Brightfield Athletics and fitness is Hosting a Spring Renewal yoga class. World-renowned Tobe Garrowen will be teaching. Tobe is a Life Empowerment Coach. This event will take place on January 5th, 2019 Time: 2pm - 4pmYoga at Brightfield Athletics and FitnessCost: $30 / $40 at the Door

Requirements
Must have
• Brightfield Athletics and fitness Logo
• Brightfield Lantern Yoga Logo

```html
<!DOCTYPE html>
<html lang="en">
<head>
<meta charset="utf-8">
<title>Spring Renewal Yoga Class — Brightfield Athletics and Fitness</title>
<link rel="stylesheet" href="https://fonts.googleapis.com/css2?family=Lato:ital,wght@0,300;0,400;1,700&family=Oswald:wght@300;400&display=swap">
<style>
  :root {
    --red: #e31e2a;
    --ink: #3d3d3f;
    --bg-top: #f3f2f0;
    --bg-mid: #ecebe9;
    --bg-low: #dedddb;
    --photo-dark: #8a8a8a;
    --photo-mid: #c4c3c1;
  }
  * { margin: 0; padding: 0; box-sizing: border-box; }
  html, body { width: 858px; height: 1200px; overflow: hidden; }
  body { background: var(--bg-mid); }

  .poster {
    position: relative;
    width: 858px;
    height: 1200px;
    overflow: hidden;
    background: linear-gradient(180deg, var(--bg-top) 0%, var(--bg-mid) 60%, var(--bg-low) 66%, #e6e5e3 100%);
    font-family: "Lato", sans-serif;
  }

  /* Photo areas */
  .instructor-photo {
    position: absolute;
    left: 520px; top: 80px;
    width: 338px; height: 610px;
    background: radial-gradient(ellipse 60% 55% at 62% 45%, var(--photo-dark) 0%, var(--photo-mid) 55%, rgba(236,235,233,0) 100%);
  }
  .student-photo {
    position: absolute;
    left: 94px; top: 712px;
    width: 680px; height: 460px;
    background: radial-gradient(ellipse 55% 50% at 68% 50%, #a9a8a6 0%, #cfcecc 55%, rgba(230,229,227,0) 100%);
  }

  /* Brand */
  .brand {
    position: absolute;
    left: 258px; top: 19px;
    display: flex; align-items: center; gap: 14px;
  }
  .brand-dot {
    width: 94px; height: 94px; border-radius: 50%;
    background: var(--red);
  }
  .brand-name {
    color: var(--red);
    font-weight: 400;
    line-height: 1;
  }
  .brand-name .line-main { display: block; font-size: 40px; letter-spacing: 0.5px; }
  .brand-name .line-sub { display: block; font-size: 15px; letter-spacing: 3px; margin-top: 6px; }

  /* Title */
  .title { position: absolute; left: 0; top: 0; width: 100%; }
  .title span { position: absolute; display: block; line-height: 1; white-space: nowrap; }
  .title-season { left: 24px; top: 146px; font-size: 50px; font-weight: 300; color: var(--red); }
  .title-theme { left: 22px; top: 210px; font-size: 118px; font-weight: 400; color: var(--red); letter-spacing: -2px; }
  .title-yoga { left: 50px; top: 318px; font-size: 128px; font-weight: 300; color: var(--red); letter-spacing: 2px; }
  .title-class { left: 222px; top: 406px; font-size: 128px; font-weight: 300; color: var(--ink); letter-spacing: 2px; }
  .byline {
    position: absolute; right: 311px; top: 519px;
    font-size: 31px; font-style: italic; font-weight: 700; color: var(--red);
    line-height: 1; white-space: nowrap;
  }

  /* Details */
  .detail {
    position: absolute; left: 34px;
    padding-left: 26px;
    border-left: 5px solid var(--red);
    font-family: "Oswald", sans-serif;
    font-weight: 300;
    line-height: 1;
  }
  .detail.is-grey { border-left-color: var(--ink); }
  .detail p { white-space: nowrap; }
  .red { color: var(--red); }
  .ink { color: var(--ink); }

  .detail-date { top: 588px; height: 158px; }
  .date-day { font-size: 38px; padding-top: 6px; }
  .date-year { font-size: 96px; margin-top: 8px; }

  .detail-time { top: 785px; height: 163px; }
  .time-label { font-size: 76px; font-weight: 400; }
  .time-range { font-size: 40px; margin-top: 8px; }
  .time-venue { font-size: 29px; margin-top: 6px; }

  .detail-cost { top: 978px; height: 163px; }
  .cost-label { font-size: 34px; padding-top: 4px; }
  .cost-prices { font-size: 70px; margin-top: 4px; }
  .cost-door { font-size: 29px; margin-top: 2px; }
</style>
</head>
<body>
<main class="poster">
  <div class="instructor-photo" role="img" aria-label="Black and white portrait of the instructor in a bandana and hoodie, arms crossed"></div>
  <div class="student-photo" role="img" aria-label="Black and white photo of a woman in a seated twisting yoga pose"></div>

  <header class="brand">
    <span class="brand-dot"></span>
    <p class="brand-name">
      <span class="line-main">BRIGHTFIELD</span>
      <span class="line-sub">ATHLETICS AND FITNESS</span>
    </p>
  </header>

  <h1 class="title">
    <span class="title-season">SPRING</span>
    <span class="title-theme">RENEWAL</span>
    <span class="title-yoga">YOGA</span>
    <span class="title-class">CLASS</span>
  </h1>
  <p class="byline">by Tobe Garrowen</p>

  <section class="detail detail-date">
    <p class="date-day red">January 5th,</p>
    <p class="date-year ink">2019</p>
  </section>

  <section class="detail detail-time is-grey">
    <p class="time-label red">TIME:</p>
    <p class="time-range ink">2pm - 4pm</p>
    <p class="time-venue red">at Brightfield Athletics</p>
  </section>

  <section class="detail detail-cost">
    <p class="cost-label red">FitnessCost:</p>
    <p class="cost-prices"><span class="ink">$30 / </span><span class="red">$40</span></p>
    <p class="cost-door red">at the Door</p>
  </section>
</main>
</body>
</html>
```